IT recruiter company is looking for a web design
Zielgruppe
We are an IT recruiting company. Our customers are middle to large companies from different branches.
Aufgabenstellung
We need an responsive landing page (home) like those of the competitors like Vorlant (http://vorlant.de) or LORV (http://lorv.de)
The logo is attached as PNG-file. Please let us know if you need an other format.
Would be nice if you can include the colors that are used in the logo into the design

```html
<!DOCTYPE html>
<html lang="de">
<head>
<meta charset="utf-8">
<title>Nerlyn – IT Recruiting</title>
<link href="https://fonts.googleapis.com/css2?family=Oswald:wght@400;500&family=Montserrat:wght@400;500;600&display=swap" rel="stylesheet">
<style>
:root{
  --frame:#b3b3b3;
  --white:#ffffff;
  --light:#f5f5f5;
  --blue:#3f74d0;
  --blue-soft:rgba(74,124,214,.82);
  --red:#e3063b;
  --yellow:#f6b416;
  --slate:#5f6590;
  --ink:#333333;
  --muted:#6b6b6b;
}
*{margin:0;padding:0;box-sizing:border-box}
html,body{width:684px;height:1200px;overflow:hidden;background:var(--frame)}
body{font-family:'Montserrat',sans-serif;color:var(--ink);position:relative}
.page{position:absolute;left:37px;top:23px;width:616px;height:1140px;background:var(--white);overflow:hidden}
section,header,footer{position:absolute;left:0;width:616px;overflow:hidden}
.abs{position:absolute}

.site-header{top:0;height:54px;background:var(--white)}
.nav-link{position:absolute;top:24px;font-size:8.4px;color:var(--slate);letter-spacing:.1px;white-space:nowrap}
.nav-link.active{background:var(--slate);color:var(--white);padding:2px 3px;top:22px}
.brand{position:absolute;left:257px;top:13px;display:flex;align-items:center;gap:5px}
.brand-mark{width:12px;height:12px;background:var(--red)}
.brand-name{font-family:'Montserrat',sans-serif;font-weight:600;font-size:24px;color:var(--slate);line-height:1}

.hero{top:54px;height:267px}
.hero-photo{position:absolute;inset:0;background:linear-gradient(120deg,#8ea6cf 0%,#c9cfe0 45%,#b9c6de 100%)}
.hero-panel{position:absolute;inset:0}
.hero-title{position:absolute;left:371px;top:85px;font-family:'Oswald',sans-serif;font-weight:400;font-size:29px;line-height:30px;letter-spacing:2px;color:var(--white)}
.hero-text{position:absolute;left:371px;top:148px;width:205px;font-size:9.2px;line-height:10.5px;color:var(--white)}
.btn{position:absolute;height:23px;display:flex;align-items:center;justify-content:center;font-size:6.6px;font-weight:500;color:var(--white);border-radius:2px;letter-spacing:.3px}
.btn-blue{background:var(--blue)}
.btn-red{background:var(--red)}

.section-title{position:absolute;font-family:'Oswald',sans-serif;font-size:17px;letter-spacing:1.6px;line-height:1;display:flex;align-items:center;gap:4px;white-space:nowrap}
.chev{width:7px;height:12px}

.jobs{top:321px;height:213px;background:var(--light)}
.job-list{position:absolute;left:55px;top:78px;list-style:none;font-size:7.6px;line-height:14.6px}
.job-list b{font-weight:600;color:var(--ink)}
.job-list .sep{color:var(--red);font-weight:600}
.job-list span.loc{color:var(--muted)}
.career-text{position:absolute;left:373px;top:81px;width:204px;font-size:7.5px;line-height:9.6px;color:var(--muted);text-align:justify}

.about{top:534px;height:178px}
.about-photo{position:absolute;inset:0;background:linear-gradient(100deg,#9fa8b4 0%,#c7ccd2 50%,#dde1e6 100%)}
.about-text{position:absolute;left:54px;top:60px;width:121px;font-size:7.5px;line-height:9.6px;color:var(--white);text-align:justify}

.stats{top:712px;height:186px;background:var(--light)}
.stat{position:absolute;top:70px;width:160px;text-align:center;font-family:'Oswald',sans-serif}
.stat-num{font-size:40px;font-weight:500;color:var(--slate);line-height:44px;letter-spacing:1px}
.stat-label{font-size:12px;font-weight:500;letter-spacing:1.5px;color:var(--ink);line-height:14px}

.contact{top:898px;height:204px}
.contact-photo{position:absolute;inset:0;background:linear-gradient(90deg,#5a6f95 0%,#8ea2c4 40%,#a9bbd9 100%)}
.field{position:absolute;background:rgba(74,124,214,.85);color:var(--white);font-size:7px;letter-spacing:.4px;padding:0 10px;display:flex;align-items:center}
.field.textarea{align-items:flex-start;padding-top:10px}

.site-footer{top:1102px;height:38px;background:var(--white)}
.foot-link{position:absolute;top:16px;font-size:7px;letter-spacing:.5px;color:var(--ink)}
</style>
</head>
<body>
<div class="page">

  <header class="site-header">
    <a class="nav-link" style="left:44px">ÜBER UNS</a>
    <a class="nav-link" style="left:102px">FÜR SPEZIALISTEN</a>
    <a class="nav-link" style="left:186px">FÜR KUNDEN</a>
    <div class="brand"><span class="brand-mark"></span><span class="brand-name">Nerlyn</span></div>
    <a class="nav-link active" style="left:379px">MY NERLYN</a>
    <a class="nav-link" style="left:451px">KONTAKT</a>
    <a class="nav-link" style="left:508px">BLOG</a>
  </header>

  <section class="hero">
    <div class="hero-photo" role="img" aria-label="Geschäftsmann mit Aktentasche läuft eine Treppe hinauf vor einem Bürogebäude"></div>
    <svg class="hero-panel" width="616" height="267" viewBox="0 0 616 267">
      <polygon points="380,0 616,0 616,267 262,267" fill="#4a7cd6" opacity=".88"/>
    </svg>
    <h1 class="hero-title">LOREM IPSUM<br>DOLOR SIT AMET</h1>
    <p class="hero-text">In ius diceret reprehendunt. lisque graecis his cu. Habeo invenire laboramus mel an.</p>
    <a class="btn btn-blue" style="left:371px;top:181px;width:98px">JETZT INFORMIEREN</a>
  </section>

  <section class="jobs">
    <h2 class="section-title" style="left:43px;top:46px">
      <svg class="chev" viewBox="0 0 7 12"><path d="M1 0 L7 6 L1 12 L3 6 Z" fill="var(--red)"/></svg>RECENT JOBS
    </h2>
    <ul class="job-list">
      <li><b>Jawa Entwickler</b> <span class="sep">/</span> <span class="loc">Berlin, Deutschland</span></li>
      <li><b>Technical Support Specialist</b> <span class="sep">/</span> <span class="loc">Leimen, Deutschland</span></li>
      <li><b>Linux Engineer</b> <span class="sep">/</span> <span class="loc">St. Gallen, Schweiz</span></li>
    </ul>
    <a class="btn btn-red" style="left:55px;top:140px;width:98px">ALLE JOBS ANZEIGEN</a>

    <h2 class="section-title" style="left:361px;top:46px">
      <svg class="chev" viewBox="0 0 7 12"><path d="M1 0 L7 6 L1 12 L3 6 Z" fill="var(--blue)"/></svg>KARRIERE CENTER
    </h2>
    <p class="career-text">Lorem ipsum dolor sit amet, illud nominati mel ad, assum temporibus vim ad. At equidem ullamcorper eam, tota illum facilisis mei at. An laudem persecuti mea. lisque graecis his cu. Habeo invenire.</p>
    <a class="btn btn-blue" style="left:372px;top:140px;width:98px">FÜR KUNDEN</a>
    <a class="btn btn-blue" style="left:479px;top:140px;width:98px">FÜR SPEZIALISTEN</a>
  </section>

  <section class="about">
    <div class="about-photo" role="img" aria-label="Team arbeitet an Schreibtischen mit Computern in einem offenen Büro"></div>
    <svg class="abs" style="left:0;top:0" width="616" height="178" viewBox="0 0 616 178">
      <polygon points="0,0 267,0 187,178 0,178" fill="#5d8ad8" opacity=".88"/>
    </svg>
    <h2 class="section-title" style="left:43px;top:28px;color:var(--white)">
      <svg class="chev" viewBox="0 0 7 12"><path d="M1 0 L7 6 L1 12 L3 6 Z" fill="var(--yellow)"/></svg>ÜBER UNS
    </h2>
    <p class="about-text">Lorem ipsum dolor sit amet, illud nominati mel ad, assum temporibus vim ad. At equidem ullamcorper eam, tota illum facilisis mei at.</p>
    <a class="btn btn-blue" style="left:55px;top:120px;width:98px">KONTAKT</a>
  </section>

  <section class="stats">
    <div class="stat" style="left:74px"><div class="stat-num">1 372</div><div class="stat-label">JOBS</div></div>
    <div class="stat" style="left:227px"><div class="stat-num">428</div><div class="stat-label">BRANCH</div></div>
    <div class="stat" style="left:379px"><div class="stat-num">5 609</div><div class="stat-label">KANDIDATEN</div></div>
  </section>

  <section class="contact">
    <div class="contact-photo" role="img" aria-label="Mann im blauen Hemd telefoniert am Schreibtisch"></div>
    <svg class="abs" style="left:0;top:0" width="616" height="204" viewBox="0 0 616 204">
      <rect x="250" y="0" width="366" height="204" fill="#5b8ad9" opacity=".7"/>
    </svg>
    <h2 class="section-title" style="left:390px;top:24px;color:var(--white)">
      <svg class="chev" viewBox="0 0 7 12"><path d="M1 0 L7 6 L1 12 L3 6 Z" fill="var(--white)"/></svg>GET IN TOUCH
    </h2>
    <div class="field" style="left:287px;top:68px;width:156px;height:27px">NAME</div>
    <div class="field" style="left:448px;top:68px;width:157px;height:27px">E-MAIL ADRESSE *</div>
    <div class="field textarea" style="left:287px;top:101px;width:318px;height:55px">NACHRICHT</div>
    <a class="btn btn-blue" style="left:402px;top:165px;width:98px">SENDEN</a>
  </section>

  <footer class="site-footer">
    <a class="foot-link" style="left:73px">DATENSCHUTZ</a>
    <a class="foot-link" style="left:143px">IMPRESSUM</a>
    <span class="foot-link" style="left:455px">NERLYN - 2018</span>
  </footer>

</div>
</body>
</html>
```